Book Cover Design for Ember Lantern Hours: Mending Your Spirit When Someone Close Chose to Leave

I need a book cover jacket design for a new book called Ember Lantern Hours: Mending Your Spirit When Someone Close Chose to Leave.
The subject of the book is how to find balance again in your life after the suicide loss of a loved-one. I want the cover design to be in dark shades (browns, gray, variant shades) with lighter fonts for the title and for author's name. Would like to see designs with a concept of a dark tunnel with a road, a person walking down it, and a light ahead (off in the far distance) or an ominous picture of a road/journey with a person walking through the darkness. I need the final design to convey the message of journey through darkness to hope & healing.

Target Market(s)

men and women between the ages of 21-60.

Industry/Entity Type

Health And Wellness

Font styles to use
Serif
Sans Serif

Requirements
Must have
• Design must have a road or tunnel or both and a person walking towards it. It must convey a person walking into a heavy storm (sorrow), the other 1/4 to 1/2 of the book to convey hope, hopefulness, and brighter feeling, relief.
• My name at the bottom front- by Maelis Dunworth
Nice to have
• Some ideas I'd like to see:
• - Design idea to include road or tunnel. 3/4 of the book dark, ominous like storms, rain, fog, tears and convey sadness and deep sorrow; the other 1/4 of the book very light, peaceful, healing, less harsh and convey hope and positive progress ahead.
• Colors to Play with: Browns, Naturals, Grays, Darker-scale muted tones of blue
Should not have
• no red of any kind.

```html
<!DOCTYPE html>
<html lang="en">
<head>
<meta charset="utf-8">
<title>Ember Lantern Hours — Book Cover</title>
<link rel="stylesheet" href="https://fonts.googleapis.com/css2?family=Raleway:wght@200;300&family=Pinyon+Script&family=EB+Garamond:ital,wght@1,500&display=swap">
<style>
  :root {
    --ink: #000000;
    --rose-light: #f2cdbf;
    --rose-mid: #d9a295;
    --rose-deep: #b97f7a;
    --tunnel-glow: #fbf6f1;
    --tunnel-warm: #c9a39a;
    --tunnel-brown: #6b4a44;
    --tunnel-dark: #1c1313;
    --author-text: #f4f0f2;
  }
  * { margin: 0; padding: 0; box-sizing: border-box; }
  html, body {
    width: 825px;
    height: 1200px;
    overflow: hidden;
    background: var(--ink);
  }
  .cover {
    position: relative;
    width: 825px;
    height: 1200px;
    background: var(--ink);
    overflow: hidden;
  }
  .cover-photo {
    position: absolute;
    left: 0;
    top: 330px;
    width: 825px;
    height: 870px;
    display: block;
  }
  .title {
    position: absolute;
    left: 0;
    top: 0;
    width: 825px;
    height: 400px;
    font-weight: normal;
  }
  .title-main,
  .title-script {
    position: absolute;
    background: linear-gradient(100deg, var(--rose-deep) 0%, var(--rose-mid) 45%, var(--rose-light) 100%);
    -webkit-background-clip: text;
    background-clip: text;
    color: transparent;
    white-space: nowrap;
  }
  .title-main {
    left: 34px;
    top: 18px;
    font-family: "Raleway", "Helvetica Neue", sans-serif;
    font-weight: 200;
    font-size: 180px;
    line-height: 1;
    letter-spacing: 4px;
  }
  .title-script {
    right: 48px;
    top: 206px;
    font-family: "Pinyon Script", cursive;
    font-size: 104px;
    line-height: 1.1;
    padding-right: 12px;
  }
  .subtitle {
    position: absolute;
    right: 56px;
    top: 342px;
    width: 520px;
    text-align: right;
    font-family: "Raleway", "Helvetica Neue", sans-serif;
    font-weight: 300;
    font-size: 21px;
    line-height: 1.35;
    letter-spacing: 1px;
    color: var(--rose-light);
  }
  .author {
    position: absolute;
    right: 34px;
    bottom: 28px;
    font-family: "EB Garamond", Georgia, serif;
    font-style: italic;
    font-weight: 500;
    font-size: 46px;
    color: var(--author-text);
    letter-spacing: 0.5px;
  }
</style>
</head>
<body>
  <main class="cover">
    <svg class="cover-photo" role="img" aria-label="Photograph: silhouette of a man standing inside a dark brick tunnel, facing a bright opening of light at its far end" viewBox="0 0 825 870" preserveAspectRatio="none">
      <defs>
        <radialGradient id="tunnel-light" cx="427" cy="520" r="520" gradientUnits="userSpaceOnUse">
          <stop offset="0" stop-color="var(--tunnel-glow)"/>
          <stop offset="0.2" stop-color="var(--tunnel-glow)"/>
          <stop offset="0.32" stop-color="var(--tunnel-warm)"/>
          <stop offset="0.6" stop-color="var(--tunnel-brown)"/>
          <stop offset="0.88" stop-color="var(--tunnel-dark)"/>
          <stop offset="1" stop-color="var(--ink)"/>
        </radialGradient>
        <linearGradient id="top-fade" x1="0" y1="0" x2="0" y2="1">
          <stop offset="0" stop-color="#000" stop-opacity="1"/>
          <stop offset="0.25" stop-color="#000" stop-opacity="0"/>
          <stop offset="0.85" stop-color="#000" stop-opacity="0"/>
          <stop offset="1" stop-color="#000" stop-opacity="0.7"/>
        </linearGradient>
      </defs>
      <rect width="825" height="870" fill="url(#tunnel-light)"/>
      <rect width="825" height="870" fill="url(#top-fade)"/>
    </svg>

    <h1 class="title">
      <span class="title-main">Ember</span>
      <span class="title-script">Lantern Hours</span>
    </h1>
    <p class="subtitle">Mending Your Spirit When Someone Close Chose to Leave</p>

    <p class="author">by Maelis Dunworth</p>
  </main>
</body>
</html>
```